Business Card and Simple Logo Desgin

New Zealand based start up company "Brook Advisory LTD" requires business cards and simple logo design.

Card Content.

Brook Advisory LTD

Joanna Pritchard
CA, BMS (Hons)

j.pritchard@brookadvisory.co.nz
PH +64 21 574 160

Target Market(s)

Corporate Business in IT, Finance and accounting.

Industry/Entity Type

Business

```html
<!DOCTYPE html>
<html lang="en">
<head>
<meta charset="utf-8">
<title>Brook Advisory LTD — Business Card</title>
<link rel="stylesheet" href="https://fonts.googleapis.com/css2?family=Source+Sans+3:wght@400;600&display=swap">
<style>
  :root {
    --backdrop: #2a2a2a;
    --card-white: #ffffff;
    --card-grey: #eceeef;
    --rule-green: #3f8a4a;
    --rule-light: #cfe3d2;
    --band-blue: #2a9ed6;
    --band-blue-deep: #1878b8;
    --brand-navy: #2b3f99;
    --brand-green: #2f9a3e;
    --text-light: #ffffff;
    --text-soft: #e4f3fb;
  }
  * { box-sizing: border-box; margin: 0; padding: 0; }
  html, body {
    width: 1200px;
    height: 900px;
    overflow: hidden;
    background: var(--backdrop);
    font-family: "Source Sans 3", "Myriad Pro", sans-serif;
  }
  .stage {
    width: 1200px;
    height: 900px;
    display: flex;
    align-items: center;
    justify-content: center;
  }
  .business-card {
    position: relative;
    width: 840px;
    height: 480px;
    border-radius: 22px;
    overflow: hidden;
    background: linear-gradient(180deg, var(--card-white) 0%, var(--card-grey) 100%);
    box-shadow: 0 20px 50px rgba(0,0,0,0.5);
  }
  .card-header {
    position: absolute;
    top: 0; left: 0; right: 0;
    height: 262px;
  }
  .brand {
    position: absolute;
    left: 46px;
    top: 74px;
    display: flex;
    align-items: center;
    gap: 16px;
  }
  .brand-dot {
    width: 54px;
    height: 54px;
    border-radius: 50%;
    background: var(--brand-green);
  }
  .brand-name {
    font-size: 40px;
    font-weight: 600;
    color: var(--brand-navy);
    letter-spacing: 0.2px;
  }
  .card-rule {
    position: absolute;
    left: 0; right: 0;
    top: 262px;
    height: 10px;
    background: linear-gradient(180deg, var(--rule-light) 0%, var(--rule-green) 60%);
  }
  .card-band {
    position: absolute;
    left: 0; right: 0;
    top: 272px;
    bottom: 0;
    background: radial-gradient(ellipse at 55% 20%, var(--band-blue) 0%, var(--band-blue-deep) 100%);
    padding: 26px 0 0 52px;
    color: var(--text-light);
  }
  .person-name {
    font-size: 36px;
    font-weight: 400;
    line-height: 1.1;
  }
  .person-credentials {
    font-size: 24px;
    color: var(--text-soft);
    margin-top: 6px;
  }
  .contact {
    margin-top: 38px;
    font-size: 24px;
    line-height: 1.25;
    color: var(--text-light);
  }
</style>
</head>
<body>
  <main class="stage">
    <article class="business-card">
      <header class="card-header">
        <div class="brand">
          <span class="brand-dot"></span>
          <span class="brand-name">Brook Advisory LTD</span>
        </div>
      </header>
      <div class="card-rule"></div>
      <section class="card-band">
        <h1 class="person-name">Joanna Pritchard</h1>
        <p class="person-credentials">CA, BMS (Hons)</p>
        <div class="contact">
          <p class="contact-phone">PH +64 21 574 160</p>
          <p class="contact-email">j.pritchard@brookadvisory.co.nz</p>
        </div>
      </section>
    </article>
  </main>
</body>
</html>
```